KORVELTA Corporate Business Card

Modern business card design for company which focuses in the areas of Staffing, IT Consulting & Data Services. Please note: We are no longer using the IT subscript on the logo. All designs should have IT subscript removed.
Website: www.korveltait.example

```html
<!DOCTYPE html>
<html lang="en">
<head>
<meta charset="utf-8">
<title>KORVELTA Corporate Business Card</title>
<link href="https://fonts.googleapis.com/css2?family=Quicksand:wght@500;700&family=Arimo:wght@400&display=swap" rel="stylesheet">
<style>
  :root {
    --stage: #2b2b2b;
    --sky: #1d9bd8;
    --sky-deep: #1890cc;
    --navy: #0a5b99;
    --brand: #1a8fd0;
    --ink: #3a3a3a;
    --paper: #ffffff;
  }
  * { margin: 0; padding: 0; box-sizing: border-box; }
  html, body { width: 1200px; height: 903px; overflow: hidden; }
  body { background: var(--stage); position: relative; font-family: "Quicksand", sans-serif; }

  .card {
    position: absolute;
    width: 520px;
    height: 297px;
    border-radius: 16px;
    overflow: hidden;
    box-shadow: 0 10px 30px rgba(0,0,0,.45);
  }

  /* Back of card */
  .card-back { left: 70px; top: 110px; background: var(--sky); }
  .card-back .pattern-field {
    position: absolute; inset: 0;
    background: linear-gradient(135deg, var(--sky) 0%, var(--sky-deep) 100%);
  }
  .card-back .mark {
    position: absolute; right: 44px; top: 118px;
    display: flex; align-items: center; gap: 8px;
    color: var(--paper);
    font-family: "Quicksand", sans-serif; font-weight: 700; font-size: 20px;
    letter-spacing: 1px;
  }
  .card-back .mark .dot { width: 12px; height: 12px; background: var(--paper); }
  .services {
    position: absolute; left: 40px; bottom: 34px;
    display: flex; align-items: center; gap: 12px;
    font-family: "Arimo", sans-serif; font-size: 17px; color: var(--paper);
  }
  .services .sep { width: 7px; height: 7px; background: var(--paper); }

  /* Front of card */
  .card-front { left: 610px; top: 496px; background: var(--paper); }
  .card-front .stripe {
    position: absolute; left: 0; top: 0; bottom: 0; width: 46px; background: var(--navy);
  }
  .wordmark {
    position: absolute; left: 62px; top: 34px;
    display: flex; align-items: center; gap: 10px;
    color: var(--brand); font-weight: 700; font-size: 44px; letter-spacing: 2px;
  }
  .wordmark .dot { width: 16px; height: 16px; background: var(--brand); }
  .contact {
    position: absolute; right: 28px; top: 128px; text-align: right;
  }
  .contact .person { color: var(--brand); font-weight: 700; font-size: 21px; line-height: 1.1; }
  .contact .role { color: var(--navy); font-weight: 700; font-size: 13px; margin-bottom: 10px; }
  .contact .line {
    display: flex; justify-content: flex-end; align-items: center; gap: 6px;
    color: var(--ink); font-weight: 500; font-size: 13.5px; line-height: 1.45;
  }
  .contact .line svg { width: 11px; height: 11px; flex: none; }
  .contact .address { margin-top: 4px; padding-right: 17px; }
</style>
</head>
<body>

  <section class="card card-back">
    <div class="pattern-field" role="img" aria-label="Faint repeating brand pattern on blue"></div>
    <div class="mark"><span class="dot"></span>KORVELTA</div>
    <div class="services">
      <span>Staffing</span><span class="sep"></span>
      <span>IT Consulting</span><span class="sep"></span>
      <span>Data Services</span>
    </div>
  </section>

  <section class="card card-front">
    <div class="stripe"></div>
    <div class="wordmark"><span class="dot"></span>KORVELTA</div>
    <div class="contact">
      <div class="person">Marcus Reyland</div>
      <div class="role">President</div>
      <div class="line">555-014-2290
        <svg viewBox="0 0 12 12"><rect x="3" y="0.8" width="6" height="10.4" rx="1.2" fill="none" stroke="var(--brand)" stroke-width="1.4"/></svg>
      </div>
      <div class="line">contactus@korveltait.example
        <svg viewBox="0 0 12 12"><rect x="0.5" y="2" width="11" height="8" fill="var(--brand)"/><path d="M0.5 2 6 6.5 11.5 2" fill="none" stroke="#fff" stroke-width="1"/></svg>
      </div>
      <div class="line">www.korveltait.example
        <svg viewBox="0 0 12 12"><circle cx="6" cy="6" r="5.5" fill="var(--brand)"/><path d="M0.5 6h11M6 0.5c-2.5 3-2.5 8 0 11M6 0.5c2.5 3 2.5 8 0 11" fill="none" stroke="#fff" stroke-width="0.8"/></svg>
      </div>
      <div class="line address">418 Harlow Ave., Brenton Falls, IN 40000</div>
    </div>
  </section>

</body>
</html>
```